Sticker(s) for a chase dawn road trip

We need a bumper sticker sz and style design with the word - mkbtrz.
I envision the v with a red heart in it, a black background white lettering...but I'm open to other creative flow.
We have a custom Alberta lic plate with mkbtrz for our 1977 KR van on its way. Could also get fun with a copy of lic plate design.
Please include our website on it as well: mkbtrz.ca
Thank you!!! :)))

```html
<!DOCTYPE html>
<html lang="en">
<head>
<meta charset="utf-8">
<title>mkbtrz.ca bumper sticker</title>
<link rel="stylesheet" href="https://fonts.googleapis.com/css2?family=Archivo:wght@200;700;800&display=swap">
<style>
  :root {
    --canvas: #ffffff;
    --sticker-blue: #37c1f1;
    --wordmark: #ffffff;
    --ink: #111111;
    --label: #1a1a1a;
  }
  html, body {
    margin: 0;
    padding: 0;
    width: 1200px;
    height: 900px;
    overflow: hidden;
    background: var(--canvas);
  }
  .artboard {
    position: relative;
    width: 1200px;
    height: 900px;
  }
  .size-label {
    position: absolute;
    left: 184px;
    top: 278px;
    margin: 0;
    font-family: "Archivo", sans-serif;
    font-weight: 200;
    font-size: 28px;
    letter-spacing: -0.5px;
    color: var(--label);
  }
  .sticker {
    position: absolute;
    left: 186px;
    top: 315px;
    width: 828px;
    height: 270px;
    background: var(--sticker-blue);
  }
  .wordmark {
    position: absolute;
    left: 0;
    right: 0;
    top: 62px;
    margin: 0;
    text-align: center;
    font-family: "Archivo", sans-serif;
    font-weight: 800;
    font-size: 128px;
    line-height: 1;
    letter-spacing: 1px;
    color: var(--wordmark);
  }
  .tagline {
    position: absolute;
    left: 0;
    right: 0;
    top: 205px;
    margin: 0;
    text-align: center;
    font-family: "Archivo", sans-serif;
    font-weight: 700;
    font-size: 34px;
    line-height: 1;
    letter-spacing: 5px;
    color: var(--ink);
    text-transform: uppercase;
  }
</style>
</head>
<body>
  <main class="artboard">
    <p class="size-label">11.5 x 3.75</p>
    <section class="sticker">
      <h1 class="wordmark">mkbtrz.ca</h1>
      <p class="tagline">chase dawn</p>
    </section>
  </main>
</body>
</html>
```